Veltrix Global Policy Document/Report Template for consistent document outputs

We need a policy document/report template that we can disseminate to staff so all produced documents look the same, and less formatting has to be done each time a policy or report is started.
VGL applies the power of biological science, physical science, and IT to solve the most challenging mission problems encompassing Forensics, Biometrics, Weapons Technical and Identity Intelligence, CBRNE, CWMD, and Public Health initiatives. Here is a list of requirements for the document:
• Cover page
o Include full logo
o Title
o Possibly a subtitle
o Version #
o Date
o We want a common look that all policy documents will follow, and it is easy to recognize
o Some color and a unique look and feel
• Header and Footer (2nd page on)
o Both header and footer must include this language: “Confidential and Proprietary - For Veltrix Global Internal Use Only,” so it appears at the top and bottom of the page
o The document title must be in either the header or footer
• Header (after first page)
o Include logo
• Footer (not counting title page)
o Must include date, and page X of Y
• 4 levels of headings, numbered 1, 1.1, 1.1.1, 1.1.1.1
• 4 levels of bullets with color/style
• Design for a callout box
• Design or a box containing a quote
• Two table designs
• Pages (other than the title page)
o Pages are primarily white
o Colors for accent and visual interest

Finally, our corporate font is Source Sans Pro.
The swirl pattern on our logo has no special meaning (but feel free to use it as a design element).

Font styles to use
Other font styles liked:
• Source Sans Pro

Requirements
Must have
• See description for more information: Cover page, header and footer, multiple heading levels, callout box, tables

```html
<!DOCTYPE html>
<html lang="en">
<head>
<meta charset="utf-8">
<title>VGL Word Template Design</title>
<link href="https://fonts.googleapis.com/css2?family=Source+Sans+3:wght@300;400;600;700&family=Montserrat:wght@600&display=swap" rel="stylesheet">
<style>
:root{
  --navy:#2b2a72;
  --purple:#6a2367;
  --red:#c41e3a;
  --red-bright:#ef1b42;
  --gold:#a58a4a;
  --grey-cell:#e6e6e8;
  --text:#2a2a2a;
  --muted:#8c8c8c;
  --brand-gradient:linear-gradient(90deg,var(--navy) 0%,var(--navy) 45%,var(--purple) 72%,var(--red-bright) 100%);
}
*{box-sizing:border-box;margin:0;padding:0}
html,body{width:1200px;height:1104px;overflow:hidden}
body{
  position:relative;
  font-family:"Source Sans 3",sans-serif;
  color:var(--text);
  background:radial-gradient(ellipse at 30% 0%,#cfcfcf 0%,#9b9b9b 45%,#6c6c6c 100%);
}
.page{position:absolute;width:348px;height:492px;background:#fff;overflow:hidden;box-shadow:0 4px 14px rgba(0,0,0,.28)}
.page--cover{left:41px;top:38px}
.page--blank-title{left:426px;top:38px}
.page--content{left:812px;top:38px}
.page--tables{left:41px;top:571px}
.page--blank{left:426px;top:571px}

/* cover */
.cover-topbar{position:absolute;left:162px;top:0;width:186px;height:12px;background:var(--navy)}
.cover-photo{position:absolute;width:79px;height:66px}
.photo-fingerprint{left:0;top:81px;background:linear-gradient(135deg,#0d3f5c,#2bb7c9 60%,#0b2a44)}
.photo-lab{left:79px;top:148px;background:linear-gradient(160deg,#0f2d55,#3f7fb8 50%,#d19b4c)}
.photo-dna{left:0;top:214px;background:linear-gradient(150deg,#031a45,#1f6fc5 55%,#061833)}
.photo-tubes{left:79px;top:280px;background:linear-gradient(120deg,#e8f3f7,#9fd0e0 55%,#c9732b)}
.photo-forensics{left:0;top:345px;background:linear-gradient(140deg,#2a2a2a,#9a9a9a 55%,#3c3c3c)}
.cover-brand{position:absolute;left:205px;top:56px;font-size:46px;font-weight:700;color:var(--navy);line-height:1;letter-spacing:-1px}
.cover-title-band{position:absolute;left:82px;top:218px;width:266px;height:58px;background:var(--brand-gradient);overflow:hidden}
.cover-title-band::after{content:"";position:absolute;right:0;top:0;width:45%;height:100%;background:repeating-linear-gradient(180deg,rgba(255,255,255,0) 0 3px,rgba(255,255,255,.22) 3px 4px)}
.cover-title{position:absolute;left:13px;top:10px;color:#fff;font-size:19px;font-weight:600;line-height:1;letter-spacing:.2px}
.cover-subtitle-box{position:absolute;left:162px;top:280px;width:140px;height:65px;background:linear-gradient(90deg,#d3d3d3,#f2f2f2 70%,#fff)}
.cover-subtitle{position:absolute;left:12px;top:20px;font-size:11px;font-weight:600;color:#222;line-height:1.15}
.cover-meta{position:absolute;left:174px;font-size:6px;color:#222}
.cover-meta--version{top:424px}
.cover-meta--date{top:444px;font-weight:700}
.cover-rule{position:absolute;left:174px;top:469px;width:174px;height:1.2px;background:var(--gold)}
.cover-confidential{position:absolute;left:174px;top:476px;font-size:4.6px}
.cover-bottombar{position:absolute;left:0;top:480px;width:157px;height:12px;background:var(--red)}

/* header parts */
.corner-square{position:absolute;left:0;top:0;width:12px;height:12px;background:var(--red)}
.corner-square--side{top:24px;width:13px}
.title-band{position:absolute;left:12px;top:12px;width:300px;height:25px;background:var(--brand-gradient)}
.title-band-text{position:absolute;left:16px;top:5px;color:#fff;font-size:13px;font-weight:600;letter-spacing:.2px}
.header-confidential{position:absolute;left:27px;top:43px;font-size:4.8px;letter-spacing:.5px}
.header-band{position:absolute;left:98px;top:24px;width:212px;height:12px;background:var(--brand-gradient)}
.checker span{position:absolute;width:12px;height:12px}
.checker .c-red{background:var(--red)}
.checker .c-navy{background:var(--navy)}
.header-brand{position:absolute;left:34px;top:18px;font-size:21px;font-weight:700;color:var(--navy);line-height:1}
.side-tagline{position:absolute;left:324px;top:82px;height:360px;writing-mode:vertical-rl;transform:rotate(180deg);font-size:5.6px;letter-spacing:5.2px;color:var(--muted);white-space:nowrap;text-align:center}

/* footer */
.footer-rule{position:absolute;left:28px;top:469px;width:278px;height:1.2px;background:var(--gold)}
.footer-rule--wide{left:27px;width:293px}
.footer-confidential{position:absolute;left:28px;top:476px;font-size:4.6px}
.footer-divider{position:absolute;left:202px;top:473px;width:1px;height:10px;background:var(--red)}
.footer-date{position:absolute;left:225px;top:476px;font-size:4.8px;font-weight:700}
.page-badge{position:absolute;left:308px;top:464px;width:20px;height:20px;border-radius:50%;border:1.6px solid var(--navy);font-size:7px;font-weight:700;display:flex;align-items:center;justify-content:center}

/* headings + body */
.h1{position:absolute;left:30px;top:79px;font-size:19px;font-weight:300;color:var(--gold)}
.h2{position:absolute;left:30px;font-size:11px;font-weight:600;color:var(--red)}
.h3{position:absolute;left:30px;font-size:9px;font-weight:600;color:var(--navy)}
.h4{position:absolute;left:30px;font-size:7.6px;font-weight:700;color:#111}
.body-copy{position:absolute;left:30px;width:282px;font-size:5.9px;line-height:7.6px}
.bullets{position:absolute;left:45px;top:310px;list-style:none}
.bullets li{font-size:6px;font-weight:700;height:10.5px;display:flex;align-items:center;gap:5px}
.bullets li::before{content:"";width:4px;height:4px;border-radius:50%;border:1.3px solid var(--purple);background:radial-gradient(circle,var(--red) 35%,#fff 40%)}
.bubble{position:absolute}
.bubble-text{position:absolute;font-size:5.8px;line-height:7.6px;text-align:center}

/* tables */
.data-table{position:absolute;left:43px;width:228px;border-collapse:collapse;font-size:6px}
.data-table th{height:20px;color:#fff;font-size:7.2px;font-weight:600;text-align:center}
.data-table th:first-child{text-align:left;padding-left:7px}
.data-table td{height:19px;text-align:center}
.data-table td:first-child{text-align:left;padding-left:7px;width:54px}
.table--navy{top:82px}
.table--navy thead tr{background:var(--navy);border-top:2px solid var(--red)}
.table--navy tbody tr{border-bottom:1.6px solid var(--red)}
.table--navy td:first-child{background:var(--grey-cell)}
.table--red{top:331px}
.table--red thead tr{background:var(--red);border-top:2px solid var(--gold)}
.table--red tbody tr{border-bottom:1.6px solid var(--gold)}
.table--red td:not(:first-child){background:var(--grey-cell)}
.callout{position:absolute;top:218px;border-radius:12px;padding:10px 12px;font-size:5.8px;line-height:7.6px;border:2.5px solid transparent;background:linear-gradient(#fff,#fff) padding-box,linear-gradient(135deg,var(--navy) 40%,var(--red)) border-box}
.callout--wide{left:40px;width:165px;height:93px}
.callout--narrow{left:217px;width:90px;height:93px;padding:10px 10px}

/* presentation label */
.label-panel{position:absolute;left:812px;top:748px;width:388px;height:159px;background:linear-gradient(90deg,#2f2f2f,#474747)}
.label-text{position:absolute;left:39px;top:32px;font-family:"Montserrat",sans-serif;font-weight:600;font-size:30px;line-height:30px;color:#fff}
</style>
</head>
<body>

<section class="page page--cover">
  <div class="cover-topbar"></div>
  <div class="cover-photo photo-fingerprint" role="img" aria-label="Photo of a fingertip touching a glowing fingerprint scan"></div>
  <div class="cover-photo photo-lab" role="img" aria-label="Photo of scientists working in a laboratory"></div>
  <div class="cover-photo photo-dna" role="img" aria-label="Photo of a glowing DNA helix above a tablet"></div>
  <div class="cover-photo photo-tubes" role="img" aria-label="Photo of test tubes with a dropper"></div>
  <div class="cover-photo photo-forensics" role="img" aria-label="Photo of a forensic investigator collecting evidence"></div>
  <div class="cover-brand">VGL</div>
  <div class="cover-title-band"><h1 class="cover-title">INTERNATIONAL<br>POLICY REPORT</h1></div>
  <div class="cover-subtitle-box"><p class="cover-subtitle">International Policy<br>Report Sample</p></div>
  <p class="cover-meta cover-meta--version">VERSION # <b>1</b></p>
  <p class="cover-meta cover-meta--date">WEDNESDAY, MARCH 20, 2024</p>
  <div class="cover-rule"></div>
  <p class="cover-confidential">Confidential and Proprietary - For Veltrix Global Internal Use Only</p>
  <div class="cover-bottombar"></div>
</section>

<section class="page page--blank-title">
  <div class="corner-square"></div>
  <div class="title-band"><span class="title-band-text">INTERNATIONAL POLICY REPORT</span></div>
  <p class="header-confidential">Confidential and Proprietary - For Veltrix Global Internal Use Only</p>
  <div class="checker"><span class="c-red" style="left:324px;top:24px"></span><span class="c-navy" style="left:312px;top:36px"></span><span class="c-navy" style="left:336px;top:36px"></span><span class="c-red" style="left:324px;top:48px"></span></div>
  <div class="footer-rule footer-rule--wide"></div>
  <p class="footer-confidential" style="left:27px">Confidential and Proprietary - For Veltrix Global Internal Use Only</p>
</section>

<section class="page page--content">
  <div class="corner-square corner-square--side"></div>
  <div class="header-brand">VGL</div>
  <div class="header-band"></div>
  <div class="checker"><span class="c-red" style="left:324px;top:24px"></span><span class="c-navy" style="left:312px;top:36px"></span><span class="c-navy" style="left:336px;top:36px"></span><span class="c-red" style="left:324px;top:48px"></span></div>
  <div class="side-tagline">Advancing Science for Safer Outcomes</div>

  <h1 class="h1">1.&nbsp; International Policy Report</h1>
  <h2 class="h2" style="top:107px">1.1 Subheading</h2>
  <p class="body-copy" style="top:126px">We need a policy document/report template that we can disseminate to staff so all produced documents look the same, and less formatting has to be done each time a policy or report is started. VGL applies the power of biological science, physical science, and IT to solve the most challenging mission problems encompassing Forensics, Biometrics, Weapons Technical and Identity Intelligence, CBRNE, CWMD, and Public Health initiatives. Here is a list of requirements for the document</p>
  <h3 class="h3" style="top:174px">1.1.1 Subheading</h3>
  <p class="body-copy" style="top:192px">We need a policy document/report template that we can disseminate to staff so all produced documents look the same, and less formatting has to be done each time a policy or report is started. VGL applies the power of biological science, physical science, and IT to solve the most challenging mission problems encompassing Forensics, Biometrics, Weapons Technical and Identity Intelligence, CBRNE, CWMD, and Public Health initiatives. Here is a list of requirements for the document</p>
  <h4 class="h4" style="top:241px">1.1.1.1 Subheading</h4>
  <p class="body-copy" style="top:258px">We need a policy document/report template that we can disseminate to staff so all produced documents look the same, and less formatting has to be done each time a policy or report is started. VGL applies the power of biological science, physical science, and IT to solve the most challenging mission problems encompassing Forensics, Biometrics, Weapons Technical and Identity Intelligence, CBRNE, CWMD, and Public Health initiatives. Here is a list of requirements for the document</p>
  <ul class="bullets"><li>Bullet</li><li>Bullet</li><li>Bullet</li><li>Bullet</li></ul>

  <svg class="bubble" style="left:28px;top:370px" width="120" height="80" viewBox="0 0 120 80">
    <defs><linearGradient id="bubbleGradA" x1="0" y1="0" x2="1" y2="1"><stop offset="0" stop-color="#c41e3a"/><stop offset="1" stop-color="#2b2a72"/></linearGradient></defs>
    <ellipse cx="60" cy="37" rx="55" ry="31" fill="none" stroke="url(#bubbleGradA)" stroke-width="2.2"/>
    <path d="M14 54 L6 70 L24 62" fill="#fff" stroke="#2b2a72" stroke-width="2.2" stroke-linejoin="round"/>
  </svg>
  <p class="bubble-text" style="left:48px;top:389px;width:80px">We need a policy document/report template that we can disseminate to staff so all produced documents look</p>

  <svg class="bubble" style="left:184px;top:322px" width="116" height="126" viewBox="0 0 116 126">
    <defs><linearGradient id="bubbleGradB" x1="0" y1="0" x2="1" y2="1"><stop offset="0" stop-color="#c41e3a"/><stop offset="1" stop-color="#2b2a72"/></linearGradient></defs>
    <circle cx="58" cy="62" r="54" fill="none" stroke="url(#bubbleGradB)" stroke-width="2.4"/>
    <path d="M94 100 L108 114 L86 106" fill="#fff" stroke="#2b2a72" stroke-width="2.4" stroke-linejoin="round"/>
  </svg>
  <p class="bubble-text" style="left:206px;top:358px;width:72px">We need a policy document/report template that we can disseminate to staff so all produced documents look the same, and less formatting has to be</p>

  <div class="footer-rule"></div>
  <p class="footer-confidential">Confidential and Proprietary - For Veltrix Global Internal Use Only</p>
  <div class="footer-divider"></div>
  <p class="footer-date">Wednesday, March 20, 2024</p>
  <div class="page-badge">1</div>
</section>

<section class="page page--tables">
  <div class="corner-square corner-square--side"></div>
  <div class="header-brand">VGL</div>
  <div class="header-band"></div>
  <div class="checker"><span class="c-red" style="left:324px;top:24px"></span><span class="c-navy" style="left:312px;top:36px"></span><span class="c-navy" style="left:336px;top:36px"></span><span class="c-red" style="left:324px;top:48px"></span></div>
  <div class="side-tagline">Advancing Science for Safer Outcomes</div>

  <table class="data-table table--navy">
    <thead><tr><th>City or Town</th><th>Point A</th><th>Point B</th><th>Point C</th><th>Point D</th><th>Point E</th></tr></thead>
    <tbody>
      <tr><td>Point A</td><td>+</td><td>-</td><td>NA</td><td>20</td><td>NA</td></tr>
      <tr><td>Point B</td><td>87</td><td>-</td><td>-</td><td>50</td><td>-</td></tr>
      <tr><td>Point C</td><td>64</td><td>56</td><td>-</td><td>NA</td><td>-</td></tr>
      <tr><td>Point D</td><td>37</td><td>32</td><td>91</td><td>5</td><td>+</td></tr>
      <tr><td>Point E</td><td>93</td><td>35</td><td>54</td><td>20</td><td>30</td></tr>
    </tbody>
  </table>

  <div class="callout callout--wide">We need a policy document/report template that we can disseminate to staff so all produced documents look the same, and less formatting has to be We need a policy document/report template that we can disseminate to staff so all produced documents look the same, and less formatting has to be We need a policy document/report template that we can disseminate to staff so all produced documents look the same, and less formatting has to be</div>
  <div class="callout callout--narrow">We need a policy document/report template that we can disseminate to staff so all produced documents look the same, and less formatting has to be We need a policy do all produced documents</div>

  <table class="data-table table--red">
    <thead><tr><th>City or Town</th><th>Point A</th><th>Point B</th><th>Point C</th><th>Point D</th><th>Point E</th></tr></thead>
    <tbody>
      <tr><td>Point A</td><td>+</td><td>-</td><td>NA</td><td>20</td><td>NA</td></tr>
      <tr><td>Point B</td><td>87</td><td>-</td><td>-</td><td>50</td><td>-</td></tr>
      <tr><td>Point C</td><td>64</td><td>56</td><td>-</td><td>NA</td><td>-</td></tr>
      <tr><td>Point D</td><td>37</td><td>32</td><td>91</td><td>5</td><td>+</td></tr>
      <tr><td>Point E</td><td>93</td><td>35</td><td>54</td><td>20</td><td>30</td></tr>
    </tbody>
  </table>

  <div class="footer-rule"></div>
  <p class="footer-confidential">Confidential and Proprietary - For Veltrix Global Internal Use Only</p>
  <div class="footer-divider"></div>
  <p class="footer-date">Wednesday, March 20, 2024</p>
  <div class="page-badge">2</div>
</section>

<section class="page page--blank">
  <div class="corner-square corner-square--side"></div>
  <div class="header-brand">VGL</div>
  <div class="header-band"></div>
  <div class="checker"><span class="c-red" style="left:324px;top:24px"></span><span class="c-navy" style="left:312px;top:36px"></span><span class="c-navy" style="left:336px;top:36px"></span><span class="c-red" style="left:324px;top:48px"></span></div>
  <div class="side-tagline">Advancing Science for Safer Outcomes</div>
  <div class="footer-rule"></div>
  <p class="footer-confidential">Confidential and Proprietary - For Veltrix Global Internal Use Only</p>
  <div class="footer-divider"></div>
  <p class="footer-date">Wednesday, March 20, 2024</p>
  <div class="page-badge">3</div>
</section>

<aside class="label-panel">
  <p class="label-text">VGL WORD<br>TEMPLATE<br>DESIGN</p>
</aside>

</body>
</html>
```